i would like a business card to leave with customers and potential customers for electrical work and for the supply and install of reverse cycle airconditioning in the domestic and commercial market.
I own my own business and im a sole trader. I have an a'class electrical lisence and also a refrigeration lisence so i am
able to offer complete installations in airconditioning by a fully qualified and lisenced tradesman.
im looking for something that comes across as unique and professional.
i had the coluor black and some gold in mind but open to any coluors.
something like Beacon Electrical & Refrigeration
or Beacon Air.
i will use this design on a business card to advertise through summer to help generate installs through the busy season.

Target Market(s)

Mainly domestic house holds through summer who are in need of airconditioning and reliable information to acomadate thier cooling and heating requirements

Industry/Entity Type

Electrical

Requirements
Must have
• Business name- Beacon
My name- Peter Wollaston
My mobile no- 0457 819 302
My email- prwollaston@tarvel.com.au
Installation & Decomissioning of aiconditioning split systems
LIC NO: KTR 407516
Nice to have
• Beacon Electrical & Refrigeration

```html
<!DOCTYPE html>
<html lang="en">
<head>
<meta charset="utf-8">
<title>Beacon Electrical &amp; Refrigeration – Business Card</title>
<link rel="stylesheet" href="https://fonts.googleapis.com/css2?family=Michroma&family=Roboto:wght@500;700&display=swap">
<style>
  :root {
    --backdrop: #2b2b2b;
    --card: #050505;
    --card-texture: #151515;
    --accent: #29aae1;
    --white: #ffffff;
    --tick-box: #d9d9d9;
    --tick: #3aa845;
  }
  * { box-sizing: border-box; margin: 0; padding: 0; }
  html, body {
    width: 1200px; height: 626px; overflow: hidden;
    background: var(--backdrop);
  }
  .canvas { position: relative; width: 1200px; height: 626px; }
  .card {
    position: absolute; top: 292px;
    width: 522px; height: 300px;
    border-radius: 14px;
    overflow: hidden;
    background: var(--card);
  }
  .card--front { left: 52px; }
  .card--back { left: 616px; }
  .card__texture {
    position: absolute; inset: 0 0 25px 0;
    background: radial-gradient(ellipse at 60% 35%, var(--card-texture), var(--card) 70%);
  }
  .card__band {
    position: absolute; left: 0; right: 0; bottom: 0; height: 25px;
    background: var(--accent);
  }
  .brand {
    position: absolute; left: 0; right: 0; text-align: center;
    font-family: "Michroma", sans-serif;
    white-space: nowrap;
  }
  .brand__name { color: var(--accent); letter-spacing: 2px; line-height: 1; }
  .brand__tagline { color: var(--white); letter-spacing: 1px; font-variant: small-caps; line-height: 1; }
  .card--front .brand { top: 100px; }
  .card--front .brand__name { font-size: 50px; }
  .card--front .brand__tagline { font-size: 16px; margin-top: 26px; }
  .card--back .brand { top: 48px; }
  .card--back .brand__name { font-size: 32px; }
  .card--back .brand__tagline { font-size: 9.5px; margin-top: 14px; }

  .holder {
    position: absolute; top: 144px; left: 0; right: 0; text-align: center;
    font-family: "Michroma", sans-serif; white-space: nowrap;
  }
  .holder__name {
    display: inline-block;
    color: var(--accent);
    font-size: 13px; line-height: 1;
    letter-spacing: 1px;
    padding: 0 14px 4px;
    border-bottom: 1px solid var(--accent);
  }
  .contact {
    position: absolute; top: 184px;
    display: flex; align-items: center; gap: 7px;
    font-family: "Roboto", sans-serif; font-weight: 700;
    color: var(--white);
    font-size: 13px; line-height: 16px; letter-spacing: 0.5px;
    white-space: nowrap;
  }
  .contact--phone { left: 74px; }
  .contact--email { left: 237px; }
  .services {
    position: absolute; top: 206px; left: 68px;
    display: flex; gap: 4px; align-items: flex-start;
    font-family: "Roboto", sans-serif; font-weight: 700;
    color: var(--white);
    font-size: 12px; line-height: 13px;
    white-space: nowrap;
  }
  .services__licence span { color: var(--accent); letter-spacing: 1px; }
</style>
</head>
<body>
<main class="canvas">
  <section class="card card--front" aria-label="Business card front">
    <div class="card__texture" role="img" aria-label="Dark geometric tile texture"></div>
    <div class="brand">
      <div class="brand__name">BEACON</div>
      <div class="brand__tagline">Beacon Electrical &amp; Refrigeration</div>
    </div>
    <div class="card__band"></div>
  </section>

  <section class="card card--back" aria-label="Business card back">
    <div class="card__texture" role="img" aria-label="Dark geometric tile texture"></div>
    <div class="brand">
      <div class="brand__name">BEACON</div>
      <div class="brand__tagline">Beacon Electrical &amp; Refrigeration</div>
    </div>
    <div class="holder"><span class="holder__name">PETER WOLLASTON</span></div>
    <div class="contact contact--phone">
      <svg width="10" height="16" viewBox="0 0 10 16" aria-hidden="true">
        <rect x="1" y="1" width="8" height="14" rx="1.5" fill="none" stroke="#fff" stroke-width="1.4"/>
        <line x1="4" y1="13" x2="6" y2="13" stroke="#fff" stroke-width="1.2"/>
      </svg>
      <span>0457 819 302</span>
    </div>
    <div class="contact contact--email">
      <svg width="16" height="11" viewBox="0 0 16 11" aria-hidden="true">
        <rect x="0.7" y="0.7" width="14.6" height="9.6" fill="none" stroke="#fff" stroke-width="1.2"/>
        <polyline points="1,1 8,6.5 15,1" fill="none" stroke="#fff" stroke-width="1.2"/>
      </svg>
      <span>PRWOLLASTON@TARVEL.COM.AU</span>
    </div>
    <div class="services">
      <svg width="22" height="22" viewBox="0 0 22 22" aria-hidden="true">
        <rect x="1" y="1" width="20" height="20" fill="var(--tick-box)"/>
        <polyline points="4,11 9,17 19,3" fill="none" stroke="var(--tick)" stroke-width="3"/>
      </svg>
      <div>
        <div>Installation &amp; Decomissioning of airconditioning split systems</div>
        <div class="services__licence">LIC NO: <span>KTR 407516</span></div>
      </div>
    </div>
    <div class="card__band"></div>
  </section>
</main>
</body>
</html>
```